Banner Ad Designs for tick and flea products

We sell tick and flea products online and want some great banner designs for our online website to promote our tick and flea products.

The ads must be made up in both Flash and HTML5
Ads can be formatted as .JPEG or .GIF files.

Please see the following url for creative requirements
http://help.bannerquay.com/creative-requirements/

Creative licence no limits to your imagination!

Ads must be created in the following sizes:

- Banner – 468×60
- Square – 250×250
- Small Square – 200×200
- Leaderboard – 728×90
- Medium Rectangle – 300×250
- Chatterbox – 100×72

please view our website at www.harbourlanepawstore.com.au or .com to get a feel for our website.

The aim is to attract customers who want to save on tick and flea purchases for their pets (dogs and cats)

Target Market(s)

Anyone who owns a dog or cat

Industry/Entity Type

Online

Font styles to use
Sans Serif
Other font styles liked:
• creative licence on font styles

Requirements
Must have
• Must have a strong urge to entice customers to click through.

Images wording and text etc use creative lic
Nice to have
• Strong appeal to dog and cat owners and how they can save on flea and tick essentials.
Keep it simple but effective.
Be fun and playful and inviting.
Should not have
• Please do not use words like cheap - cheapest

Strobing & Flashing - Strobing, flashing backgrounds, or otherwise distracting ads are not allowed. Do not attempt to overtly distract the user from page content.

```html
<!DOCTYPE html>
<html lang="en">
<head>
<meta charset="utf-8">
<title>Harbour Lane Paw Store – Leaderboard Frames</title>
<link rel="stylesheet" href="https://fonts.googleapis.com/css2?family=Arimo:wght@400;700&display=swap">
<style>
  :root {
    --page-bg: #ffffff;
    --label-blue: #1a6fc2;
    --leaf-green: #0c9a1a;
    --magenta: #f01fb4;
    --rose-edge: #d8184a;
    --panel-white: #ffffff;
    --navy: #08336e;
    --sky-edge: #1a6fd6;
    --brand-ink: #1b2a4a;
    --brand-dot: #1a4e8a;
    --headline: #ffffff;
    --button-top: #c8f25a;
    --button-bottom: #5aa61a;
    --button-ink: #1f4a0c;
    --button-icon: #2e6a12;
    --frame-line: #2b2b2b;
  }
  * { box-sizing: border-box; margin: 0; padding: 0; }
  html, body {
    width: 1200px; height: 988px; overflow: hidden;
    background: var(--page-bg);
    font-family: "Arimo", Arial, sans-serif;
  }
  .canvas { position: relative; width: 1200px; height: 988px; }

  .frame-label {
    position: absolute; left: 17px; width: 120px;
    font-size: 23px; color: var(--label-blue); line-height: 1;
  }

  .leaderboard {
    position: absolute; left: 148px; width: 1028px; height: 127px;
    outline: 1px solid var(--frame-line); overflow: hidden;
  }
  .leaderboard-shapes { position: absolute; inset: 0; width: 100%; height: 100%; }

  .pet-photo {
    position: absolute; top: 6px; left: 7px; width: 184px; height: 116px;
    border-radius: 6px;
    background: linear-gradient(100deg, #3a2418 0%, #8a6a4e 40%, #b9a893 65%, #e9e4de 100%);
  }
  .pug-photo {
    position: absolute; top: 0; right: 0; width: 145px; height: 127px;
    background: linear-gradient(90deg, #c9a774 0%, #e3c99a 45%, #b58c58 100%);
  }

  .brand {
    position: absolute; left: 210px; top: 50px;
    display: flex; align-items: center; gap: 7px;
  }
  .brand-dot { width: 16px; height: 16px; border-radius: 50%; background: var(--brand-dot); }
  .brand-name { font-size: 20px; font-weight: 700; color: var(--brand-ink); white-space: nowrap; }

  .headline {
    position: absolute; left: 410px; width: 410px; text-align: center;
    color: var(--headline); font-weight: 700;
    text-shadow: 1px 2px 2px rgba(0,0,0,0.75);
  }
  .headline--a { top: 12px; font-size: 29px; line-height: 31px; }
  .headline--b { top: 5px; font-size: 35px; line-height: 35px; }
  .headline--c { top: 12px; font-size: 29px; line-height: 31px; }

  .order-button {
    position: absolute; left: 527px; top: 63px; width: 166px; height: 50px;
    border-radius: 6px;
    background: linear-gradient(180deg, var(--button-top) 0%, var(--button-bottom) 100%);
    box-shadow: 0 0 0 2px rgba(255,255,255,0.35) inset, 0 2px 3px rgba(0,0,0,0.4);
    display: flex; align-items: center; justify-content: center; gap: 8px;
  }
  .order-button-text { font-size: 17px; font-weight: 700; color: var(--button-ink); }
  .order-button-icon {
    width: 30px; height: 30px; border-radius: 4px; background: var(--button-icon);
    display: flex; align-items: center; justify-content: center;
  }
</style>
</head>
<body>
<main class="canvas">

  <!-- Frame A -->
  <span class="frame-label" style="top:270px;">FRAME A</span>
  <section class="leaderboard" style="top:217px;" aria-label="Frame A">
    <svg class="leaderboard-shapes" viewBox="0 0 728 90" preserveAspectRatio="none" aria-hidden="true">
      <rect width="728" height="90" fill="var(--leaf-green)"/>
      <path d="M0 0 H268 Q296 45 268 90 H0 Z" fill="var(--rose-edge)"/>
      <path d="M0 0 H262 Q289 45 262 90 H0 Z" fill="var(--magenta)"/>
      <path d="M5 4 H262 Q284 45 262 86 H5 Z" fill="var(--panel-white)"/>
      <path d="M728 0 H588 Q568 45 588 90 H728 Z" fill="var(--sky-edge)"/>
      <path d="M728 0 H594 Q575 45 594 90 H728 Z" fill="var(--navy)"/>
    </svg>
    <div class="pet-photo" role="img" aria-label="Photo of a small dog resting on a tabby cat"></div>
    <div class="brand"><span class="brand-dot"></span><span class="brand-name">Harbour Lane</span></div>
    <p class="headline headline--a">Save On Genuine<br>Brand Tick And<br>Flea Protection</p>
    <div class="pug-photo" role="img" aria-label="Photo of three pugs in collars"></div>
  </section>

  <!-- Frame B -->
  <span class="frame-label" style="top:412px;">FRAME B</span>
  <section class="leaderboard" style="top:360px;" aria-label="Frame B">
    <svg class="leaderboard-shapes" viewBox="0 0 728 90" preserveAspectRatio="none" aria-hidden="true">
      <rect width="728" height="90" fill="var(--leaf-green)"/>
      <path d="M0 0 H268 Q296 45 268 90 H0 Z" fill="var(--rose-edge)"/>
      <path d="M0 0 H262 Q289 45 262 90 H0 Z" fill="var(--magenta)"/>
      <path d="M5 4 H262 Q284 45 262 86 H5 Z" fill="var(--panel-white)"/>
      <path d="M728 0 H588 Q568 45 588 90 H728 Z" fill="var(--sky-edge)"/>
      <path d="M728 0 H594 Q575 45 594 90 H728 Z" fill="var(--navy)"/>
    </svg>
    <div class="pet-photo" role="img" aria-label="Photo of a small dog resting on a tabby cat"></div>
    <div class="brand"><span class="brand-dot"></span><span class="brand-name">Harbour Lane</span></div>
    <p class="headline headline--b">Protect Your Pets<br>From Ticks and<br>Fleas</p>
    <div class="pug-photo" role="img" aria-label="Photo of three pugs in collars"></div>
  </section>

  <!-- Frame C -->
  <span class="frame-label" style="top:554px;">FRAME C</span>
  <section class="leaderboard" style="top:501px;" aria-label="Frame C">
    <svg class="leaderboard-shapes" viewBox="0 0 728 90" preserveAspectRatio="none" aria-hidden="true">
      <rect width="728" height="90" fill="var(--leaf-green)"/>
      <path d="M0 0 H268 Q296 45 268 90 H0 Z" fill="var(--rose-edge)"/>
      <path d="M0 0 H262 Q289 45 262 90 H0 Z" fill="var(--magenta)"/>
      <path d="M5 4 H262 Q284 45 262 86 H5 Z" fill="var(--panel-white)"/>
      <path d="M728 0 H588 Q568 45 588 90 H728 Z" fill="var(--sky-edge)"/>
      <path d="M728 0 H594 Q575 45 594 90 H728 Z" fill="var(--navy)"/>
    </svg>
    <div class="pet-photo" role="img" aria-label="Photo of a small dog resting on a tabby cat"></div>
    <div class="brand"><span class="brand-dot"></span><span class="brand-name">Harbour Lane</span></div>
    <p class="headline headline--c">Save And Order Online</p>
    <div class="order-button">
      <span class="order-button-text">ORDER NOW</span>
      <span class="order-button-icon">
        <svg width="12" height="12" viewBox="0 0 12 12" aria-hidden="true"><path d="M3 1 L10 6 L3 11 Z" fill="#ffffff"/></svg>
      </span>
    </div>
    <div class="pug-photo" role="img" aria-label="Photo of three pugs in collars"></div>
  </section>

</main>
</body>
</html>
```